Website design for learning and development business

I need a logo for my new business based in Australasia. I am a kiwi who is a creative change maker working in the Learning & development space. I design experiential learning opportunities for businesses to grow and nurture their tribes. I take a holistic look at an organisation and analyse what is needed to build a positive culture with a growth mindset woven into their DNA. I would like to see designs that are based on the following word snaps - creative, interesting, tribal, journey, adaptability, engaging, fluid, architectural, bespoke, courageous, challenging .I have the logo (attached) and I Need a startup business website designed. I am a Learning and development professional who is looking at going out on my own and establishing my own business. I would like a website designed that people would go to to check out what I do, how I do, what skills I have and how to contact me. Also room for a blog/articles.

Target Market(s)

Small to medium business

Industry/Entity Type

Self employed training and consultancy company

Number of Pages Required

5+ page

Requirements
Must have
• home page, about page, contact us page, blog page, search for us page
Nice to have
• Testimonials,

```html
<!DOCTYPE html>
<html lang="en">
<head>
<meta charset="utf-8">
<title>Tribewise — Training and Consultancy</title>
<link href="https://fonts.googleapis.com/css2?family=Barlow+Semi+Condensed:wght@400;500;600&family=Roboto:ital,wght@0,400;0,500;0,700;1,400&display=swap" rel="stylesheet">
<style>
:root{
  --blue:#1a73c3;
  --green:#9bc832;
  --red:#e6391f;
  --nav:#1f1f1f;
  --ink:#222;
  --muted:#444;
  --soft:#f5f5f5;
  --dark:#3d3a3b;
  --white:#fff;
}
*{box-sizing:border-box;margin:0;padding:0}
html,body{width:1200px;height:3619px;overflow:hidden}
body{position:relative;background:var(--white);font-family:"Roboto",sans-serif;color:var(--ink)}
.abs{position:absolute}
.head{font-family:"Barlow Semi Condensed",sans-serif;font-weight:500;text-transform:uppercase;color:var(--ink)}
.head em{font-style:normal;color:var(--blue)}
.pill{position:absolute;border:1.5px solid var(--blue);border-radius:20px;color:var(--blue);font-family:"Barlow Semi Condensed",sans-serif;font-weight:600;font-size:13px;letter-spacing:.6px;display:flex;align-items:center;justify-content:center;text-transform:uppercase;background:transparent}
.center{left:0;width:1200px;text-align:center}

/* header */
.brand{left:62px;top:46px;display:flex;align-items:center;gap:10px;font-family:"Barlow Semi Condensed",sans-serif;font-weight:600;font-size:30px;color:var(--blue)}
.brand-dot{width:26px;height:26px;border-radius:50%;background:var(--blue)}
.call{left:765px;top:24px;font-family:"Barlow Semi Condensed",sans-serif;font-size:19px;font-weight:500}
.call span{color:var(--blue)}
.nav{left:0;top:80px;width:1200px;height:40px}
.nav-item{position:absolute;top:80px;height:40px;line-height:40px;color:#fff;font-family:"Barlow Semi Condensed",sans-serif;font-weight:600;font-size:13.5px;letter-spacing:.6px;text-transform:uppercase;transform:translateX(-50%)}

/* hero */
.hero-photo{left:0;top:120px;width:1200px;height:540px;background:linear-gradient(180deg,#7c7f82 0%,#5d6064 45%,#3f4246 100%)}
.hero-title{top:314px;font-family:"Barlow Semi Condensed",sans-serif;font-weight:500;font-size:39px;line-height:46px;color:#fff;text-transform:uppercase;letter-spacing:.5px}
.btn-solid{position:absolute;background:var(--blue);color:#fff;border-radius:16px;font-family:"Barlow Semi Condensed",sans-serif;font-weight:600;font-size:13px;letter-spacing:.6px;display:flex;align-items:center;justify-content:center;text-transform:uppercase}

/* welcome */
.welcome-accent{left:208px;top:944px;width:184px;height:264px;background:var(--green)}
.welcome-photo{left:232px;top:728px;width:352px;height:456px;border-radius:18px 40px 60px 0;background:linear-gradient(160deg,#c9cdd2 0%,#8e8681 50%,#6b6a6e 100%)}
.lead{left:664px;top:818px;width:340px;font-size:16.5px;line-height:26px;color:var(--muted)}
.small{left:664px;top:942px;width:340px;font-size:10.8px;line-height:19.3px;color:var(--muted)}

/* services */
.services{left:0;top:1287px;width:1200px;height:640px;background:var(--soft)}
.svc{position:absolute;top:1476px;width:270px;text-align:center;transform:translateX(-50%)}
.svc h3{margin-top:86px;font-family:"Barlow Semi Condensed",sans-serif;font-weight:400;font-size:19px;color:var(--ink)}
.svc p{margin-top:18px;font-size:11.8px;line-height:19.3px;color:var(--muted)}
.svc-go{position:absolute;top:1708px;width:32px;height:32px;border-radius:50%;background:var(--blue);transform:translateX(-50%);display:flex;align-items:center;justify-content:center}
.divider{position:absolute;top:1472px;width:1px;height:280px;background:#e2e2e2}

/* articles */
.card{position:absolute;top:2101px;width:240px;height:399px;border:1px solid #e2e2e2;border-radius:0 0 44px 0;background:#fff}
.card-photo{width:240px;height:272px;border-radius:0 0 44px 0}
.card-date{position:absolute;left:22px;top:295px;font-size:10.5px;color:var(--blue)}
.card-title{position:absolute;left:22px;top:322px;width:200px;font-size:12px;font-weight:700;line-height:19.4px;color:#333}

/* testimonial */
.testi{left:0;top:2650px;width:1200px;height:430px;background:var(--dark)}
.quote{top:2808px;font-size:16.5px;font-style:italic;line-height:29px;color:#eee}
.avatar{left:568px;top:2881px;width:64px;height:64px;border-radius:50%;background:linear-gradient(180deg,#d8c5b5,#8c7a6d);border:2px solid #fff}

/* newsletter */
.news{left:0;top:3078px;width:1200px;height:120px;background:var(--blue)}
.field{position:absolute;border:1px solid #8e8a8b;color:#ddd;font-size:11px;padding:12px 20px}

/* footer */
.footer{left:0;top:3198px;width:1200px;height:421px;background:var(--dark)}
.f-head{font-family:"Barlow Semi Condensed",sans-serif;font-weight:500;font-size:19px;color:#fff}
.f-link{left:584px;font-size:11px;color:#e2e2e2}
.social{position:absolute;top:3456px;width:38px;height:38px;border-radius:50%;background:var(--blue)}
</style>
</head>
<body>

<!-- header -->
<div class="abs brand"><span class="brand-dot"></span>Tribewise</div>
<div class="abs call">Call Us. <span>(123) 555-0142</span></div>
<div class="pill" style="left:972px;top:20px;width:168px;height:32px">Get free quotes</div>

<svg class="abs nav" viewBox="0 0 1200 40" aria-hidden="true">
  <polygon points="318,0 1200,0 1200,40 295,40" fill="var(--nav)"/>
  <polygon points="318,0 465,0 442,40 295,40" fill="var(--blue)"/>
  <polygon points="1010,0 1200,0 1200,40 987,40" fill="var(--red)"/>
  <g stroke="#666" stroke-width="1.5">
    <line x1="572" y1="0" x2="549" y2="40"/>
    <line x1="700" y1="0" x2="677" y2="40"/>
    <line x1="836" y1="0" x2="813" y2="40"/>
  </g>
</svg>
<div class="nav-item" style="left:380px">Home</div>
<div class="nav-item" style="left:510px">About us</div>
<div class="nav-item" style="left:638px">Services</div>
<div class="nav-item" style="left:769px">Blog</div>
<div class="nav-item" style="left:922px">Testimonials</div>
<div class="nav-item" style="left:1096px">Search for us</div>

<!-- hero -->
<div class="abs hero-photo" role="img" aria-label="Photo of a trainer presenting to a seated group in a bright meeting room"></div>
<div class="abs center hero-title">Tribewise is a<br>self-employed training and<br>consultancy company</div>
<div class="btn-solid" style="left:532px;top:484px;width:136px;height:32px">Contact us</div>
<svg class="abs" style="left:0;top:500px" width="1200" height="160" viewBox="0 0 1200 160" aria-hidden="true">
  <path d="M0,60 C150,10 300,30 480,100 C620,150 760,150 900,90 C1020,45 1120,45 1200,90 L1200,160 L0,160 Z" fill="var(--blue)"/>
  <path d="M0,68 C150,40 300,60 480,120 C620,160 760,160 900,105 C1020,60 1120,60 1200,110 L1200,160 L0,160 Z" fill="#fff"/>
</svg>

<!-- welcome -->
<div class="abs welcome-accent"></div>
<div class="abs welcome-photo" role="img" aria-label="Photo of a woman with headphones taking notes at a laptop"></div>
<div class="abs head" style="left:664px;top:756px;font-size:28px;text-transform:uppercase">Welcome to <em>Tribewise</em></div>
<p class="abs lead">It is a long established fact that<br>a reader will be distracted by the readable content of a page when looking at its layout. The point of using Lorem Ipsum</p>
<p class="abs small">It is a long established fact that a reader will be distracted by the readable content of a page when looking at its layout. The point of using Lorem Ipsum is that it has a more-or-less normal distribution of letters, as opposed to using 'Content here, content here', making it look like readable English. Many desktop publishing packages and web page editors now use Lorem Ipsum as their default model text ...</p>
<div class="pill" style="left:664px;top:1115px;width:168px;height:32px">Discover about us</div>

<!-- services -->
<div class="abs services"></div>
<div class="abs center head" style="top:1360px;font-size:28px">Our <em>Services</em></div>
<div class="abs center" style="top:1413px;font-family:'Barlow Semi Condensed',sans-serif;font-size:15px;letter-spacing:.4px;color:#333">WE CAN PROVIDE JUST THE LEVEL OF SERVICE YOU NEED. NO MORE. NO LESS.</div>
<div class="divider" style="left:440px"></div>
<div class="divider" style="left:760px"></div>

<svg class="abs" style="left:247px;top:1480px" width="66" height="66" viewBox="0 0 66 66" fill="none" stroke="var(--blue)" stroke-width="2" aria-hidden="true">
  <rect x="3" y="3" width="60" height="44" rx="2"/><line x1="3" y1="40" x2="63" y2="40"/>
  <path d="M25 58 L28 47 M41 58 L38 47 M18 60 H48"/>
  <path d="M18 20 L33 13 L48 20 L33 27 Z"/><path d="M24 23 V31 C28 35 38 35 42 31 V23"/>
</svg>
<svg class="abs" style="left:567px;top:1480px" width="66" height="66" viewBox="0 0 66 66" fill="none" stroke="var(--blue)" stroke-width="2" aria-hidden="true">
  <rect x="16" y="3" width="46" height="28"/><path d="M26 12 H52 M26 19 H48"/>
  <circle cx="8" cy="12" r="4"/><path d="M8 16 V40 M8 22 L20 16"/>
  <g><circle cx="12" cy="47" r="4"/><circle cx="26" cy="47" r="4"/><circle cx="40" cy="47" r="4"/><circle cx="54" cy="47" r="4"/>
  <rect x="7" y="52" width="10" height="11" rx="3"/><rect x="21" y="52" width="10" height="11" rx="3"/><rect x="35" y="52" width="10" height="11" rx="3"/><rect x="49" y="52" width="10" height="11" rx="3"/></g>
</svg>
<svg class="abs" style="left:887px;top:1480px" width="66" height="66" viewBox="0 0 66 66" fill="none" stroke="var(--blue)" stroke-width="2" aria-hidden="true">
  <rect x="24" y="3" width="24" height="12" rx="2"/><path d="M30 9 H42"/>
  <circle cx="24" cy="26" r="5"/><circle cx="44" cy="28" r="5"/>
  <path d="M14 48 C14 36 34 36 34 48 M36 48 C36 38 54 38 54 48"/>
  <rect x="4" y="48" width="58" height="6"/><path d="M12 54 V64 M54 54 V64"/>
</svg>

<div class="svc" style="left:280px"><h3>eLearning</h3><p>It is a long established fact that a reader will be distracted by the readable content of a page when looking at its layout has a more-or-less normal...</p></div>
<div class="svc" style="left:600px"><h3>Training</h3><p>It is a long established fact that a reader will be distracted by the readable content of a page when looking at its layout has a more-or-less normal...</p></div>
<div class="svc" style="left:920px"><h3>Consulting</h3><p>It is a long established fact that a reader will be distracted by the readable content of a page when looking at its layout has a more-or-less normal...</p></div>

<div class="svc-go" style="left:280px"><svg width="12" height="10" viewBox="0 0 12 10" fill="none" stroke="#fff" stroke-width="1.5"><path d="M1 5 H11 M7 1 L11 5 L7 9"/></svg></div>
<div class="svc-go" style="left:600px;background:var(--green)"><svg width="12" height="10" viewBox="0 0 12 10" fill="none" stroke="#fff" stroke-width="1.5"><path d="M1 5 H11 M7 1 L11 5 L7 9"/></svg></div>
<div class="svc-go" style="left:920px"><svg width="12" height="10" viewBox="0 0 12 10" fill="none" stroke="#fff" stroke-width="1.5"><path d="M1 5 H11 M7 1 L11 5 L7 9"/></svg></div>

<svg class="abs" style="left:0;top:1780px" width="1200" height="150" viewBox="0 0 1200 150" aria-hidden="true">
  <path d="M0,50 C120,10 260,10 400,60 C500,95 560,140 620,140 C720,140 820,60 960,40 C1060,25 1140,40 1200,70 L1200,150 L0,150 Z" fill="var(--blue)"/>
  <path d="M0,58 C120,25 260,28 400,80 C500,118 560,142 620,142 C720,142 820,78 960,62 C1060,52 1140,65 1200,90 L1200,150 L0,150 Z" fill="#fff"/>
</svg>
<div class="pill" style="left:512px;top:1791px;width:176px;height:32px;background:var(--soft)">Contact us today!</div>

<!-- articles -->
<div class="abs center head" style="top:1996px;font-size:28px">Latest <em>Articles</em></div>
<div class="abs center" style="top:2049px;font-family:'Barlow Semi Condensed',sans-serif;font-size:15px;letter-spacing:.4px;color:#333">IT IS A LONG ESTABLISHED FACT THAT A READER WILL BE DISTRACTED</div>

<div class="card" style="left:208px">
  <div class="card-photo" role="img" aria-label="Photo of colleagues smiling around a laptop" style="background:linear-gradient(160deg,#e4e6e8,#a9a39e 60%,#7d766f)"></div>
  <div class="card-date">30 JAN 2021</div>
  <div class="card-title">It is a long established fact that a reader will be distracted by the readable.</div>
</div>
<div class="card" style="left:480px">
  <div class="card-photo" role="img" aria-label="Photo of a seminar audience with a raised hand" style="background:linear-gradient(160deg,#b9a58f,#6f5f55 55%,#3f3a38)"></div>
  <div class="card-date">01 FEB 2021</div>
  <div class="card-title">It is a long established fact that a reader will be distracted by the readable.</div>
</div>
<div class="card" style="left:752px">
  <div class="card-photo" role="img" aria-label="Photo of a speaker presenting beside a screen to a seated group" style="background:linear-gradient(160deg,#d6d9dc,#8d8f92 55%,#4a4c50)"></div>
  <div class="card-date">02 FEB 2021</div>
  <div class="card-title">It is a long established fact that a reader will be distracted by the readable.</div>
</div>
<div class="pill" style="left:528px;top:2541px;width:144px;height:32px">View all news</div>

<!-- testimonials -->
<div class="abs testi"></div>
<svg class="abs" style="left:0;top:2640px" width="1200" height="150" viewBox="0 0 1200 150" aria-hidden="true">
  <path d="M0,0 H1200 V90 C1100,40 980,30 860,20 C760,10 680,-5 580,15 C420,45 260,120 120,135 C70,140 30,132 0,125 Z" fill="#fff"/>
  <path d="M1200,90 C1100,40 980,30 860,20 C760,10 680,-5 580,15 C420,45 260,120 120,135 C70,140 30,132 0,125 L0,140 C40,150 90,150 140,145 C280,130 430,62 590,32 C690,15 770,28 870,38 C990,50 1100,68 1200,110 Z" fill="var(--blue)"/>
</svg>
<div class="abs center head" style="top:2740px;font-size:28px;color:#fff">What our <em>clients say</em></div>
<div class="abs center quote">
  <span style="font-style:normal;font-weight:700;color:#bbb;font-size:14px;vertical-align:top">“</span>&nbsp; It is a long established fact that a reader will be distracted by the readable<br>content of a page when looking at its layout. &nbsp;<span style="font-style:normal;font-weight:700;color:#bbb;font-size:14px;vertical-align:top">”</span>
</div>
<div class="abs avatar" role="img" aria-label="Portrait photo of the client"></div>
<div class="abs center" style="top:2964px;font-size:12.5px;font-weight:700;color:#fff">Lena Hartley</div>
<div class="abs center" style="top:2984px;font-size:12px;color:#e5e5e5">Founder</div>
<svg class="abs" style="left:1104px;top:2852px" width="12" height="50" viewBox="0 0 12 50" fill="none" stroke="#ccc" stroke-width="1.2" aria-hidden="true">
  <circle cx="6" cy="6" r="3.5"/><circle cx="6" cy="18" r="3.5"/><circle cx="6" cy="30" r="3.5"/><circle cx="6" cy="42" r="3.5"/>
</svg>

<!-- stay in touch -->
<div class="abs news"></div>
<div class="abs head" style="left:87px;top:3108px;font-size:28px;color:#fff">Stay in touch</div>
<div class="abs" style="left:87px;top:3150px;font-size:11.5px;color:#fff">Subscribe to get instant notification in your email inbox.</div>
<div class="abs" style="left:720px;top:3105px;width:392px;height:66px;background:#fff;border-radius:33px"></div>
<svg class="abs" style="left:752px;top:3131px" width="24" height="16" viewBox="0 0 24 16" fill="none" stroke="var(--blue)" stroke-width="1.6" aria-hidden="true"><rect x="1" y="1" width="22" height="14"/><path d="M1 1 L12 9 L23 1"/></svg>
<div class="abs" style="left:790px;top:3131px;font-size:12px;color:#333">you@example.com</div>
<div class="abs" style="left:1000px;top:3119px;width:96px;height:38px;border-radius:19px;background:var(--green);color:#fff;font-family:'Barlow Semi Condensed',sans-serif;font-weight:600;font-size:13px;display:flex;align-items:center;justify-content:center;letter-spacing:.5px">SIGN UP</div>

<!-- footer -->
<div class="abs footer"></div>
<div class="abs f-head" style="left:87px;top:3272px">Get Free Quotes</div>
<div class="field" style="left:87px;top:3318px;width:173px;height:38px">Your Name</div>
<div class="field" style="left:276px;top:3318px;width:172px;height:38px">Email</div>
<div class="field" style="left:87px;top:3374px;width:173px;height:38px">Phone</div>
<div class="field" style="left:276px;top:3374px;width:172px;height:38px">Subject</div>
<div class="field" style="left:87px;top:3430px;width:361px;height:95px">Message ...</div>
<div class="btn-solid" style="left:87px;top:3553px;width:169px;height:40px;border-radius:20px">Send message</div>

<div class="abs f-head" style="left:584px;top:3272px">Quick Links</div>
<div class="abs f-link" style="top:3312px">Home</div>
<div class="abs f-link" style="top:3339px">About</div>
<div class="abs f-link" style="top:3366px">Services</div>
<div class="abs f-link" style="top:3394px">Blog</div>
<div class="abs f-link" style="top:3421px">Testimonials</div>
<div class="abs f-link" style="top:3448px">Contact us</div>
<div class="abs f-link" style="top:3476px">Search for us</div>

<div class="abs f-head" style="left:778px;top:3272px">Have any Questions?</div>
<div class="abs" style="left:778px;top:3310px;font-family:'Barlow Semi Condensed',sans-serif;font-size:24px;color:#fff">Call Us. (123) 555-0142</div>
<div class="abs" style="left:778px;top:3356px;font-size:10px;color:var(--blue)">TRIBEWISE</div>
<div class="abs" style="left:778px;top:3380px;font-size:10.5px;line-height:23px;color:#e2e2e2">48 Harbour Lane Westfield, Suite 3<br>NZ 6011</div>
<div class="social" style="left:778px"></div>
<div class="social" style="left:826px;background:var(--green)"></div>
<div class="social" style="left:874px"></div>
<div class="abs" style="left:584px;top:3520px;width:528px;height:1px;background:#6a6667"></div>
<svg class="abs" style="left:1133px;top:3508px" width="14" height="18" viewBox="0 0 14 18" fill="none" stroke="var(--green)" stroke-width="1.6" aria-hidden="true"><path d="M7 17 V2 M2 7 L7 2 L12 7"/></svg>
<div class="abs" style="left:584px;top:3564px;font-size:10.5px;color:#e2e2e2">© 2021 <span style="color:#fff">Tribewise</span>. All Rights Reserved.</div>

</body>
</html>
```